Real Estate 24"x24" Sign, Business Card, Letter Head and Envelope

This is a 4 project contest. If we choose a design or designs we like from what you sent we are willing to pay an amount at our discretion for that design even if we don't like all your designs for the 4 projects. Please be creative. Attached are our logo files. Please message us with any questions. Thanks and Good Luck!
Project 1: QLTV Realty 24" x 24" yard sign
We want to use the same blue background in our logo for the sign where the logo in white font will be on. CMYK 100,80,0,0. Attached is a sample a local designer made for you to get an idea what we are looking for. In the sample, the website is way too big and the entire sign is very plain and not attractive looking plus blue color is wrong one. We want the logo on top as large as possible but keeping it proportionate and attractive looking buy not too big that it looks odd. The following information can go in white color background or same blue color background color. Our company colors are blue (as per logo), green (as per logo), and white. "Residential & Commercial" goes under the logo. Under that put our phone number "312-948-6051" as large as possible but still looks good and under that our website in much smaller but readable font "www.qltvrealty.com".
Project 2: Envelope
We have two version of the logo. Use one or both. Whatever looks best in your design. The envelope will be white. We only want on top left corner logo and underneath our mailing address: 5197 Larchmere Ave. Skokie, IL 60093-1725. Maybe some creative decorative design at bottom of envelope will look nice
Project 3: Letter Head
We have two version of the logo. Use one or both. Whatever looks best in your design. We want the following information on the top of the letterhead. Logo, address: 5197 Larchmere Ave., Skokie, IL 60093-1725, phone: 312-948-6051, fax: 312-682-9307 website www.qltvrealty.com, email: info@qltvrealty.com
Project 4: Business card
Use either logo. We need cards for two individuals. Information for Person 1: Dev Kulkarni, Managing Broker, Phone: 312-948-6051, Email: dev.kulkarni@qltvrealty.com. Person 2: Ajay Kulkarni Broker Phone: 312-519-8263 Email: ajay.kulkarni@qltvrealty.com. Add Address, Fax and website same as above letter head.

```html
<!DOCTYPE html>
<html lang="en">
<head>
<meta charset="UTF-8">
<title>QLTV Realty Envelope</title>
<link rel="stylesheet" href="https://fonts.googleapis.com/css2?family=Roboto:wght@400;700&display=swap">
<style>
  :root {
    --page-bg: #bdbdbd;
    --paper: #ffffff;
    --paper-shade: #f5f5f5;
    --brand-blue: #1450a0;
    --brand-green: #7dc242;
    --text-grey: #5a5a5a;
    --rule-grey: #cfcfcf;
  }
  * { margin: 0; padding: 0; box-sizing: border-box; }
  html, body {
    width: 1200px;
    height: 514px;
    overflow: hidden;
    background: var(--page-bg);
    font-family: "Roboto", sans-serif;
  }
  .envelope {
    position: absolute;
    left: 178px;
    top: 65px;
    width: 844px;
    height: 384px;
    background: linear-gradient(90deg, var(--paper) 0%, var(--paper-shade) 100%);
    border-radius: 2px;
    overflow: hidden;
  }
  .sender {
    position: absolute;
    left: 24px;
    top: 24px;
  }
  .brand-name {
    display: flex;
    align-items: center;
    gap: 10px;
    height: 92px;
    font-weight: 700;
    font-size: 40px;
    line-height: 1;
    color: var(--brand-blue);
    letter-spacing: 0.5px;
  }
  .brand-mark {
    width: 18px;
    height: 18px;
    background: var(--brand-green);
  }
  .mailing-address {
    margin-top: 16px;
    font-style: normal;
    font-size: 13px;
    line-height: 17px;
    color: var(--text-grey);
  }
  .footer-rule {
    position: absolute;
    left: 0;
    right: 0;
    bottom: 19px;
    height: 2px;
    background: var(--rule-grey);
  }
  .footer-band {
    position: absolute;
    left: 0;
    right: 0;
    bottom: 0;
    height: 16px;
    background: var(--brand-blue);
  }
</style>
</head>
<body>
  <div class="envelope">
    <div class="sender">
      <div class="brand-name"><span class="brand-mark"></span>QLTV Realty</div>
      <address class="mailing-address">
        5197 Larchmere Ave.<br>
        Skokie, IL 60093-1725
      </address>
    </div>
    <div class="footer-rule"></div>
    <div class="footer-band"></div>
  </div>
</body>
</html>
```